Fundraising campaign to raise money to purchase a pub

We are a voluntary group campaigning to stop a pub from becoming residential flats by fighting planning proposals. We are also raising money to buy or lease the pub to re-open it as a community pub.I have attached a mock idea for a flyer.We are seeking a flyer that we can use to handout.

The purpose of the flyer is to invite people to our public meeting and to complete our pub survey.

We are looking for an A5 flyer in terms of size

Target Market(s)

Local residents, investors

Industry/Entity Type

Residential

Font styles to use
Serif
Sans Serif
Decorative
Script

Requirements
Must have
• Be eyecatching. Must have a summary of the campaign. Must also have website date and time of the public meeting. Must also promote the survey and website. Must also have contact details. Must have the survey. The date and the survey should be easily spotted.
Nice to have
• A picture of the plough
Should not have
• Clip art

```html
<!DOCTYPE html>
<html lang="en">
<head>
<meta charset="utf-8">
<title>Safeguarding the Future of The Plough</title>
<link href="https://fonts.googleapis.com/css2?family=Oswald:wght@500;700&family=Open+Sans:wght@400;600;700;800&display=swap" rel="stylesheet">
<style>
  :root {
    --wood-dark: #2a1a12;
    --wood: #3d2718;
    --wood-light: #5a3a24;
    --header: #1f1712;
    --orange: #e8912f;
    --orange-bright: #f2a13a;
    --white: #ffffff;
    --cream: #f6eedd;
    --survey-text: #c47a22;
    --red: #b8321f;
    --red-dark: #8f2415;
  }
  * { margin: 0; padding: 0; box-sizing: border-box; }
  html, body { width: 889px; height: 1200px; overflow: hidden; background: var(--wood-dark); }
  .flyer {
    position: relative; width: 889px; height: 1200px; overflow: hidden;
    background: linear-gradient(90deg, var(--wood-dark), var(--wood) 30%, var(--wood-light) 50%, var(--wood) 70%, var(--wood-dark));
    font-family: "Open Sans", Arial, sans-serif; color: var(--white);
  }
  .masthead {
    position: absolute; left: 0; top: 0; width: 889px; height: 140px;
    background: var(--header); text-align: center; padding-top: 26px;
    border-bottom: 3px solid var(--orange);
  }
  .masthead h1 {
    font-family: "Oswald", Impact, sans-serif; font-weight: 700; font-size: 46px;
    letter-spacing: 0.5px; text-transform: uppercase; line-height: 1.1;
  }
  .masthead h2 {
    font-family: "Open Sans", Arial, sans-serif; font-weight: 700; font-size: 28px;
    color: var(--orange); margin-top: 6px;
  }
  .photo-interior {
    position: absolute; left: 28px; top: 160px; width: 833px; height: 270px;
    background: linear-gradient(180deg, #6a3f22, #9a5f2f 45%, #4a2a18);
    border: 4px solid var(--white);
  }
  .story {
    position: absolute; left: 40px; top: 446px; width: 810px;
    font-size: 14.5px; line-height: 1.45; text-align: justify;
  }
  .photo-exterior {
    position: absolute; left: 28px; top: 556px; width: 350px; height: 250px;
    background: linear-gradient(180deg, #8a8a88, #3a2a22 55%, #1c1410);
    border: 4px solid var(--white);
  }
  .mission {
    position: absolute; left: 412px; top: 566px; width: 440px;
  }
  .mission .aim { color: var(--orange); font-size: 21px; font-weight: 600; line-height: 1.3; text-align: right; }
  .mission .goal {
    font-family: "Oswald", Impact, sans-serif; font-weight: 700; font-size: 30px;
    line-height: 1.2; text-transform: uppercase; margin-top: 14px; text-align: left;
  }
  .meeting { position: absolute; left: 40px; top: 832px; width: 340px; }
  .meeting p { font-size: 14.5px; line-height: 1.45; }
  .meeting .date {
    font-family: "Oswald", Impact, sans-serif; font-weight: 700; font-size: 38px;
    color: var(--orange-bright); margin-top: 14px; line-height: 1;
  }
  .meeting .venue { font-weight: 700; font-size: 16px; margin-top: 8px; }
  .survey {
    position: absolute; left: 418px; top: 830px; width: 440px; height: 170px;
    background: var(--cream); color: var(--survey-text); padding: 16px 18px;
    font-size: 15.5px; line-height: 1.4; font-weight: 600; text-align: right;
  }
  .survey strong { color: #8a4a10; }
  .contact {
    position: absolute; left: 0; top: 1024px; width: 889px; height: 176px;
    background: linear-gradient(180deg, var(--red), var(--red-dark));
    border-top: 3px solid var(--orange);
  }
  .contact h3 {
    font-family: "Oswald", Impact, sans-serif; font-weight: 700; font-size: 40px;
    text-align: center; margin-top: 16px; text-transform: uppercase;
  }
  .contact .row {
    position: absolute; top: 100px; display: flex; align-items: center; gap: 12px;
    font-family: "Oswald", Impact, sans-serif; font-weight: 500; font-size: 28px;
  }
  .contact .email { left: 46px; }
  .contact .phone { left: 560px; }
  .icon { width: 40px; height: 40px; }
</style>
</head>
<body>
<div class="flyer">
  <header class="masthead">
    <h1>Safeguarding the future of The Plough</h1>
    <h2>Protect pubs in Eastbrook</h2>
  </header>

  <div class="photo-interior" role="img" aria-label="Photograph of the pub interior with the wooden bar, stools and tables"></div>

  <p class="story">The Plough, 55 Eastbrook High Street, EB25 was purchased by a property developer, who proceeded to gut the pub and convert it into seven flats. The developer has tried twice to obtain planning permission and now is the subject of retrospective planning to put the pub back downstairs and in the basement. Should this not be forthcoming Eastbrook Council will be issue and enforcement notice to the owner.</p>

  <div class="photo-exterior" role="img" aria-label="Photograph of the pub frontage on the high street"></div>

  <section class="mission">
    <p class="aim">Save the Plough is a campaigning to protect the building and also raise money to lease the pub or buy the building.</p>
    <p class="goal">We want to open The Plough as a community co-op pub serving great good and wine.</p>
  </section>

  <section class="meeting">
    <p>Anyone wishing to find out more about our plans to open a great pub serving fantastic food and drinks can attend our meeting</p>
    <p class="date">18 August at 8pm</p>
    <p class="venue">Harbourlight pub, Mercer Road, EB25.</p>
  </section>

  <section class="survey">
    Please support our campaign by completing our survey https://surveyhub.net/r/plough-eb25-form<br>
    Paper copies of the survey are available get a friend or relative to check on <strong>www.savetheplough.co.uk</strong> for locations.
  </section>

  <footer class="contact">
    <h3>You can contact us by</h3>
    <div class="row email">
      <svg class="icon" viewBox="0 0 40 40" aria-hidden="true">
        <circle cx="20" cy="20" r="19" fill="#fff"/>
        <rect x="9" y="13" width="22" height="15" rx="2" fill="none" stroke="#b8321f" stroke-width="2.4"/>
        <path d="M9 14 L20 22 L31 14" fill="none" stroke="#b8321f" stroke-width="2.4"/>
      </svg>
      <span>saveploughe25@mailpost.com</span>
    </div>
    <div class="row phone">
      <svg class="icon" viewBox="0 0 40 40" aria-hidden="true">
        <circle cx="20" cy="20" r="19" fill="#fff"/>
        <path d="M14 10 l4 0 l2 6 l-3 2 q2 5 6 7 l2 -3 l6 2 l0 4 q-1 3 -4 3 q-10 -1 -16 -13 q-1 -5 3 -8z" fill="#b8321f"/>
      </svg>
      <span>02080000123</span>
    </div>
  </footer>
</div>
</body>
</html>
```